MerlionTripzy

I need a website similar to http://crestvalora.example. I have the following broad requirements
1. Site should be a itinerary based singapore travel and holiday site. You can visit travquill.example for domain knowledge but not for design. Design should be exact replica of crestvalora.example
2. Site should be same as http://crestvalora.example. Links placement, Logo Placement, Forms design, scrolling, THE MAIN VIDEO LIKE GIF (required and acceptance reqd.), fonts, social links, javascript(copy not reinvent) et al. Please ask as many questions if you have queries. This is very important. I am a CS Grad so won't accept deviation because i know web programming. Design should be exact replica
3. Please use images from Creative Commons travel images from pixhaven or internet especially singapore popular destinations. images will help my sale and please ensure creative quality.
4. Cross Browser importantly IE versions because target customers may be computer illiterates
5. HTML5/css3 and follow latest Standards and practices.
6. Clean Commented HTML and css code for maintainability.

Hoping for the world's best creative and experienced professional who have done similar designs to accept my project.

Industry/Entity Type

Internet

```html
<!DOCTYPE html>
<html lang="en">
<head>
<meta charset="utf-8">
<title>MerlionTripzy – Singapore Holidays</title>
<link href="https://fonts.googleapis.com/css2?family=Josefin+Sans:wght@400;600;700&family=Open+Sans:wght@400;600&display=swap" rel="stylesheet">
<style>
:root{
  --teal:#17b8c9;
  --teal-dark:#119fae;
  --ink:#2b2b2b;
  --text:#555;
  --muted:#999;
  --band:#f1f1f1;
  --dark:#262626;
  --footer:#1e1e1e;
  --white:#fff;
}
*{box-sizing:border-box;margin:0;padding:0}
html,body{width:1200px;height:4110px;overflow:hidden}
body{position:relative;background:var(--white);font-family:"Open Sans",Arial,sans-serif;color:var(--text)}
.abs{position:absolute}
.heading{font-family:"Josefin Sans",Arial,sans-serif;font-weight:700;color:var(--teal);text-transform:uppercase;letter-spacing:1px;text-align:center}
.btn{position:absolute;display:flex;align-items:center;justify-content:center;font-family:"Josefin Sans",Arial,sans-serif;font-weight:600;font-size:15px;letter-spacing:.5px;text-transform:uppercase;color:var(--white)}
.btn-teal{background:var(--teal)}
.btn-dark{background:var(--ink)}
.copy{font-size:12px;line-height:22px;text-align:center}

/* navigation */
.site-nav{top:0;left:0;width:1200px;height:82px;background:var(--white)}
.site-nav ul{list-style:none;position:absolute;left:162px;top:32px;display:flex;gap:24px;font-family:"Josefin Sans",Arial,sans-serif;font-size:13px;font-weight:600;color:var(--ink);letter-spacing:.3px}
.site-nav .nav-cta{position:absolute;left:940px;top:30px;width:100px;height:32px;font-size:12px}

/* hero */
.hero{top:82px;left:0;width:1200px;height:384px;background:linear-gradient(180deg,#cfdbe4 0%,#a9bccb 45%,#6f8697 70%,#4d6272 100%)}
.hero-title{top:100px;width:100%;text-align:center;font-family:"Josefin Sans",Arial,sans-serif;font-weight:700;font-size:56px;color:var(--teal)}
.hero-arrow{top:170px;width:34px;height:34px;border-radius:50%;background:rgba(255,255,255,.5)}
.search{top:241px;left:260px;width:713px;height:44px;display:flex}
.search-field{flex:1;background:var(--white);font-size:13px;color:#aaa;padding:13px 16px}
.search-btn{position:relative;width:140px;height:44px;font-size:14px}
.search-note{top:299px;left:260px;font-size:11px;color:var(--white)}
.search-adv{top:299px;left:880px;font-size:11px;color:var(--white);font-weight:600}

/* how it works */
.how-title{top:510px;width:100%;font-size:20px}
.how-intro{top:562px;left:250px;width:700px}
.step{width:280px;text-align:center}
.step svg{display:block;margin:0 auto}
.step h3{margin-top:22px;font-family:"Josefin Sans",Arial,sans-serif;font-size:15px;font-weight:700;color:var(--teal);text-transform:uppercase}
.step p{margin-top:14px;font-size:11px;line-height:20px}

/* destinations */
.dest-band{top:940px;left:0;width:1200px;height:718px;background:var(--band)}
.dest-card{top:981px;left:159px;width:882px;height:636px;background:var(--white)}
.dest-title{top:1022px;width:100%;font-size:20px}
.tile{width:153px;height:200px}
.tile-photo{height:132px}
.tile-label{height:68px;background:var(--teal);color:var(--white);font-size:10px;font-weight:600;line-height:15px;padding:16px 8px}
.pager{top:1548px;font-family:"Josefin Sans",Arial,sans-serif;font-size:12px;font-weight:700;color:var(--ink);display:flex;align-items:center;gap:10px}

/* video */
.video-pack{top:1712px;left:159px;width:383px;height:310px;background:linear-gradient(135deg,#f2f2f2,#bdbdbd 55%,#8a8a8a)}
.video-title{top:1750px;left:559px;font-family:"Josefin Sans",Arial,sans-serif;font-size:20px;font-weight:700;color:var(--teal);text-transform:uppercase}
.video-copy{top:1792px;left:559px;width:480px;font-size:12px;line-height:20px}

/* stories mosaic */
.mosaic{top:2096px;left:0;width:1200px;height:501px}
.cell{position:absolute}
.quote{position:absolute;color:var(--white);font-size:15px;line-height:22px;width:260px}
.quote svg{display:block;margin-bottom:10px}
.quote .name{color:var(--teal);font-size:17px;margin-top:18px}

/* hotel rooms */
.rooms-title{top:2660px;width:100%;font-size:20px}
.rooms-copy{top:2700px;left:160px;width:880px}

/* testimonial */
.testimonial{top:2904px;left:0;width:1200px;height:288px;background:var(--dark)}
.testimonial p{position:absolute;top:124px;left:270px;width:660px;color:var(--white);font-size:14px;line-height:22px;text-align:center}
.testimonial .source{position:absolute;top:218px;width:100%;text-align:center;color:var(--teal);font-family:"Josefin Sans",Arial,sans-serif;font-weight:700;font-size:18px}
.dots{position:absolute;top:258px;left:562px;display:flex;gap:6px}
.dots i{width:10px;height:10px;border-radius:50%;background:#555}
.dots i:first-child{background:var(--teal)}

/* map */
.map{top:3192px;left:0;width:1200px;height:321px;background:linear-gradient(135deg,#e3e3e3,#d2d2d2 50%,#e8e8e8)}
.locate{top:3288px;left:444px;width:298px;height:110px;background:rgba(23,184,201,.85);color:var(--white);font-family:"Josefin Sans",Arial,sans-serif;font-weight:700;font-size:15px;text-align:center;text-transform:uppercase}

/* best hotels */
.hotels-title{top:3548px;width:100%;font-size:20px}
.hotels-sub{top:3584px;width:100%;text-align:center;font-size:14px;color:var(--muted)}
.hotel{top:3644px;width:288px}
.hotel-photo{position:relative;height:197px}
.hotel-caption{margin-top:10px;text-align:center;font-size:13px;color:var(--muted)}
.badge{position:absolute;top:0;left:0}

/* footer */
.site-footer{top:3981px;left:0;width:1200px;height:129px;background:var(--footer)}
.social{position:absolute;top:20px;left:500px;display:flex;gap:8px}
.social i{width:20px;height:20px;border-radius:50%;background:#555}
.footer-links{position:absolute;top:61px;width:100%;display:flex;justify-content:center;gap:26px;font-family:"Josefin Sans",Arial,sans-serif;font-size:12px;font-weight:600;color:var(--white)}
.footer-copy{position:absolute;top:95px;width:100%;text-align:center;font-size:11px;color:#bbb}
</style>
</head>
<body>

<header class="abs site-nav">
  <ul>
    <li>HOME</li><li>MERLIONTRIPZY</li><li>WHY ATTEND</li><li>WHO ATTENDS</li><li>WHO SPEAKS</li><li>STARTUPS</li><li>NEWS</li><li>HOTELS</li><li>CAREERS</li>
  </ul>
  <div class="btn btn-teal nav-cta">Book Now</div>
</header>

<section class="abs hero" role="img" aria-label="Singapore skyline across the bay at dusk">
  <div class="abs hero-title">MerlionTripzy</div>
  <div class="abs hero-arrow" style="left:51px"></div>
  <div class="abs hero-arrow" style="left:1112px"></div>
  <div class="abs search">
    <div class="search-field">Search Destinations Here</div>
    <div class="btn btn-teal search-btn">Search Now</div>
  </div>
  <div class="abs search-note">Clicking above indicates agreement to our terms of use</div>
  <div class="abs search-adv">Advance Search</div>
</section>

<h2 class="abs heading how-title">How It Works</h2>
<p class="abs copy how-intro">Lorem Ipsum is simply dummy text of the printing and typesetting industry. Lorem Ipsum has been the industry's standard dummy text ever since the 1500s, when an unknown printer...</p>

<div class="abs step" style="top:650px;left:142px">
  <svg width="90" height="115" viewBox="0 0 90 115" aria-hidden="true">
    <circle cx="50" cy="12" r="11" fill="#333"/>
    <path d="M38 28h24l6 40H58l-4 40h-10l-2-40h-8z" fill="#333"/>
    <rect x="8" y="62" width="30" height="36" rx="4" fill="#333"/>
    <circle cx="14" cy="104" r="5" fill="#333"/><circle cx="32" cy="104" r="5" fill="#333"/>
  </svg>
  <h3>Choose Trip</h3>
  <p>Lorem Ipsum is simply dummy text of the<br>printing and typesetting industry. Lorem Ipsum<br>has been the industry's...</p>
</div>
<div class="abs step" style="top:650px;left:463px">
  <svg width="90" height="115" viewBox="0 0 90 115" aria-hidden="true">
    <path d="M28 10a20 20 0 0 1 20 20c0 16-20 38-20 38S8 46 8 30A20 20 0 0 1 28 10z" fill="none" stroke="#333" stroke-width="6"/>
    <circle cx="28" cy="30" r="7" fill="#333"/>
    <path d="M28 80c20 0 10 20 34 18" fill="none" stroke="#333" stroke-width="5"/>
    <path d="M70 4a10 10 0 0 1 10 10c0 8-10 20-10 20S60 22 60 14A10 10 0 0 1 70 4z" fill="#333"/>
  </svg>
  <h3>Customize and Plan</h3>
  <p>Lorem Ipsum is simply dummy text of the<br>printing and typesetting industry. Lorem Ipsum<br>has been the industry's...</p>
</div>
<div class="abs step" style="top:650px;left:778px">
  <svg width="90" height="115" viewBox="0 0 90 115" aria-hidden="true">
    <path d="M80 22c4-4 4-8 0-8s-6 2-10 6L56 34 14 24l-6 6 34 18-14 14-12-2-4 4 14 8 8 14 4-4-2-12 14-14 18 34 6-6-10-42z" fill="#333"/>
  </svg>
  <h3>Book Your Trip</h3>
  <p>Lorem Ipsum is simply dummy text of the<br>printing and typesetting industry. Lorem Ipsum<br>has been the industry's...</p>
</div>

<section class="abs dest-band"></section>
<div class="abs dest-card"></div>
<h2 class="abs heading dest-title">Famous Destinations in Singapore</h2>

<div class="abs tile" style="top:1074px;left:186px"><div class="tile-photo" role="img" aria-label="Destination photo" style="background:linear-gradient(160deg,#2d3b47,#5c6f7e)"></div><div class="tile-label">Famous Destination<br>Singapore</div></div>
<div class="abs tile" style="top:1074px;left:355px"><div class="tile-photo" role="img" aria-label="Destination photo" style="background:linear-gradient(160deg,#8fb1c6,#2f5a3d)"></div><div class="tile-label">Famous Destination<br>Singapore</div></div>
<div class="abs tile" style="top:1074px;left:523px"><div class="tile-photo" role="img" aria-label="Destination photo" style="background:linear-gradient(160deg,#3a6fb6,#6aa07a)"></div><div class="tile-label">Famous Destination<br>Singapore</div></div>
<div class="abs tile" style="top:1074px;left:692px"><div class="tile-photo" role="img" aria-label="Destination photo" style="background:linear-gradient(160deg,#4f86c2,#d29a55)"></div><div class="tile-label">Famous Destination<br>Singapore</div></div>
<div class="abs tile" style="top:1074px;left:860px"><div class="tile-photo" role="img" aria-label="Destination photo" style="background:linear-gradient(160deg,#c9a777,#7b5a3a)"></div><div class="tile-label">Famous Destination<br>Singapore</div></div>

<div class="abs tile" style="top:1293px;left:186px"><div class="tile-photo" role="img" aria-label="Destination photo" style="background:linear-gradient(160deg,#a98a66,#4c3a2b)"></div><div class="tile-label">Famous Destination<br>Singapore</div></div>
<div class="abs tile" style="top:1293px;left:355px"><div class="tile-photo" role="img" aria-label="Destination photo" style="background:linear-gradient(160deg,#16263b,#b38a3e)"></div><div class="tile-label">Famous Destination<br>Singapore</div></div>
<div class="abs tile" style="top:1293px;left:523px"><div class="tile-photo" role="img" aria-label="Destination photo" style="background:linear-gradient(160deg,#b8c9d6,#9b3a2c)"></div><div class="tile-label">Famous Destination<br>Singapore</div></div>
<div class="abs tile" style="top:1293px;left:692px"><div class="tile-photo" role="img" aria-label="Destination photo" style="background:linear-gradient(160deg,#7d2d22,#3a2c24)"></div><div class="tile-label">Famous Destination<br>Singapore</div></div>
<div class="abs tile" style="top:1293px;left:860px"><div class="tile-photo" role="img" aria-label="Destination photo" style="background:linear-gradient(160deg,#c7d3db,#6f7b6a)"></div><div class="tile-label">Famous Destination<br>Singapore</div></div>

<div class="abs pager" style="left:186px">
  <svg width="12" height="14" viewBox="0 0 12 14" aria-hidden="true"><path d="M12 0v14L0 7z" fill="var(--teal)"/></svg>PREV
</div>
<div class="btn btn-dark" style="top:1529px;left:559px;width:236px;height:60px">View More Destinations</div>
<div class="abs pager" style="left:956px">
  NEXT<svg width="12" height="14" viewBox="0 0 12 14" aria-hidden="true"><path d="M0 0v14l12-7z" fill="var(--teal)"/></svg>
</div>

<div class="abs video-pack" role="img" aria-label="Video DVD case with disc"></div>
<h2 class="abs video-title">MerlionTripzy</h2>
<p class="abs video-copy">Lorem Ipsum is simply dummy text of the printing and typesetting industry. Lorem Ipsum has been the industry's standard dummy text ever since the 1500s, when an unknown printer took a galley of type and scrambled it to make a type specimen book. It has survived not only five centuries, but also the leap into electronic typesetting.</p>
<div class="btn btn-dark" style="top:1885px;left:559px;width:238px;height:60px">Download the Video</div>

<section class="abs mosaic">
  <div class="cell" style="left:0;top:0;width:310px;height:250px;background:linear-gradient(135deg,#3b3b3b,#1f1f1f)" role="img" aria-label="Traveller portrait, darkened"></div>
  <div class="cell" style="left:0;top:250px;width:310px;height:251px;background:linear-gradient(135deg,#7a8ea0,#3f4f5e)" role="img" aria-label="Businessman on the phone on a train"></div>
  <div class="cell" style="left:310px;top:0;width:315px;height:205px;background:linear-gradient(135deg,#9a8070,#c7b39e)" role="img" aria-label="Backpackers at a station"></div>
  <div class="cell" style="left:310px;top:205px;width:315px;height:296px;background:linear-gradient(135deg,#c9cfd6,#6c7480)" role="img" aria-label="Smiling travellers with backpacks"></div>
  <div class="cell" style="left:625px;top:0;width:307px;height:501px;background:linear-gradient(180deg,#8f8070,#5e5349 60%,#b6a996)" role="img" aria-label="Woman reading a map in a city street"></div>
  <div class="cell" style="left:932px;top:0;width:268px;height:300px;background:linear-gradient(135deg,#4a4541,#232120)" role="img" aria-label="Traveller portrait, darkened"></div>
  <div class="cell" style="left:932px;top:300px;width:268px;height:201px;background:linear-gradient(135deg,#e4e7ea,#9ea6ae)" role="img" aria-label="Woman with luggage at an airport"></div>

  <div class="quote" style="left:38px;top:130px">
    <svg width="22" height="22" viewBox="0 0 22 22" aria-hidden="true"><circle cx="11" cy="11" r="11" fill="#fff"/><path d="M6 14v-3l2-4h2l-1 3h2v4zm6 0v-3l2-4h2l-1 3h2v4z" fill="#222"/></svg>
    Lorem Ipsum is simply dummy text of the printing and typesetting industry.
    <div class="name">Daniel Hartono</div>
  </div>
  <div class="quote" style="left:956px;top:130px;width:240px">
    <svg width="22" height="22" viewBox="0 0 22 22" aria-hidden="true"><circle cx="11" cy="11" r="11" fill="#fff"/><path d="M6 14v-3l2-4h2l-1 3h2v4zm6 0v-3l2-4h2l-1 3h2v4z" fill="#222"/></svg>
    Lorem Ipsum is simply dummy text of the printing and typesetting industry.
    <div class="name">Daniel Hartono</div>
  </div>
</section>

<h2 class="abs heading rooms-title">Hotel Rooms Are Available</h2>
<p class="abs copy rooms-copy">Lorem Ipsum is simply dummy text of the printing and typesetting industry. Lorem Ipsum has been the industry's standard dummy text ever since the 1500s, when an unknown printer took a galley of type and scrambled it to make a type specimen book.</p>
<div class="btn btn-teal" style="top:2767px;left:529px;width:142px;height:58px">Book Now</div>

<section class="abs testimonial">
  <svg class="abs" style="top:38px;left:550px" width="100" height="70" viewBox="0 0 100 70" aria-hidden="true">
    <path d="M0 70V40C0 18 10 4 36 0l4 10C26 14 20 22 20 32h20v38zm56 0V40C56 18 66 4 92 0l4 10C82 14 76 22 76 32h20v38z" fill="#fff"/>
  </svg>
  <p>Lorem Ipsum is simply dummy text of the printing and typesetting industry. Lorem Ipsum has been the industry's standard dummy text ever since the 1500s, when an unknown printer took a galley of type and scrambled it to make a type specimen book</p>
  <div class="source">Travel Ledger</div>
  <div class="dots"><i></i><i></i><i></i><i></i><i></i></div>
</section>

<section class="abs map" role="img" aria-label="Street map of Singapore"></section>
<div class="abs locate">
  <svg style="display:block;margin:12px auto 8px" width="30" height="42" viewBox="0 0 30 42" aria-hidden="true"><path d="M15 0a15 15 0 0 1 15 15c0 12-15 27-15 27S0 27 0 15A15 15 0 0 1 15 0z" fill="#444"/><circle cx="15" cy="15" r="6" fill="#fff"/></svg>
  Select to Your Location
</div>

<h2 class="abs heading hotels-title">The Best Hotels in Singapore</h2>
<p class="abs hotels-sub">Neque porro quisquam est qui dolorem ipsum quia dolor sit amet, consectetur</p>

<div class="abs hotel" style="left:159px">
  <div class="hotel-photo" role="img" aria-label="Hotel exterior at night in black and white" style="background:linear-gradient(135deg,#6a6a6a,#1c1c1c)">
    <svg class="badge" width="60" height="60" viewBox="0 0 60 60" aria-hidden="true"><path d="M0 0h60L0 60z" fill="var(--teal)"/></svg>
    <div class="btn" style="top:80px;left:94px;width:100px;height:34px;background:#fff;color:var(--ink);font-size:12px">Book Now</div>
  </div>
  <div class="hotel-caption">Neque porro quisquam est qui</div>
</div>
<div class="abs hotel" style="left:455px">
  <div class="hotel-photo" role="img" aria-label="Hotel towers across a green waterfront" style="background:linear-gradient(180deg,#c6d3de,#6f8a6a 70%,#3b5a3e)"></div>
  <div class="hotel-caption">Neque porro quisquam est qui</div>
</div>
<div class="abs hotel" style="left:753px">
  <div class="hotel-photo" role="img" aria-label="Illuminated hotel towers at night" style="background:linear-gradient(135deg,#0f2d5a,#2a7fb8 60%,#16253b)">
    <svg class="badge" width="60" height="60" viewBox="0 0 60 60" aria-hidden="true"><path d="M0 0h60L0 60z" fill="var(--teal)"/></svg>
  </div>
  <div class="hotel-caption">Neque porro quisquam est qui</div>
</div>
<div class="btn btn-teal" style="top:3902px;left:479px;width:242px;height:55px">View All Destinations</div>

<footer class="abs site-footer">
  <div class="social"><i></i><i></i><i></i><i></i><i></i><i></i><i></i><i></i></div>
  <div class="footer-links">
    <span>ATTENDEES</span><span>STARTUPS</span><span>TICKETS</span><span>HOTELS</span><span>MEDIA</span><span>SPEAKERS</span><span>PRIVACY POLICY</span><span>INVESTORS</span><span>STUDENTS</span><span>FAQ</span><span>TOP</span>
  </div>
  <div class="footer-copy">© 2014 COMPANY NAME , ALL RIGHTS RESERVED</div>
</footer>

</body>
</html>
```